mosswickpartners Business Card Design

Business card with logo design for mosswickpartners. We are a group of professional project managers based on the Pareto Principle that 80% of the work is done by 20% of the people. I have a makeshift logo that uses a pi chart with 30% and 20% and the 20% pie slice is set slightly out and up. Have played around with a teal and orange colour scheme.

Industry/Entity Type

Business

Contact Information for Business Card

Harold Penbury
Director
mosswickpartners

0487 263019

```html
<!DOCTYPE html>
<html lang="en">
<head>
<meta charset="utf-8">
<title>mosswickpartners Business Card</title>
<link href="https://fonts.googleapis.com/css2?family=Oxanium:wght@400;500;600&display=swap" rel="stylesheet">
<style>
  :root {
    --backdrop: #e8e5e0;
    --card: #ffffff;
    --orange: #ef5a3a;
    --orange-light: #f39a3c;
    --teal: #1d8c9c;
    --ink: #2f2f33;
    --muted: #6b6b70;
    --social-a: #4a3f8e;
    --social-b: #2aa6e0;
    --social-c: #2b9bd6;
  }
  * { margin: 0; padding: 0; box-sizing: border-box; }
  html, body {
    width: 1200px; height: 828px; overflow: hidden;
    background: var(--backdrop);
    font-family: "Oxanium", "Segoe UI", sans-serif;
    color: var(--ink);
  }
  .card {
    position: absolute; left: 280px;
    width: 640px; height: 366px;
    background: var(--card);
    box-shadow: 0 6px 18px rgba(0,0,0,0.12);
    overflow: hidden;
  }
  .card--front { top: 28px; }
  .card--back { top: 434px; }

  .brand { position: absolute; display: flex; align-items: center; gap: 10px; }
  .brand__dot { width: 22px; height: 22px; border-radius: 50%; background: var(--orange); }
  .brand__name { font-size: 24px; font-weight: 500; color: var(--teal); letter-spacing: 0.5px; }
  .card--front .brand { left: 40px; top: 36px; }
  .card--back .brand { left: 50%; top: 50%; transform: translate(-50%, -50%); }
  .card--back .brand__dot { width: 30px; height: 30px; }
  .card--back .brand__name { font-size: 34px; }

  .name-band {
    position: absolute; left: 0; top: 96px; width: 250px; height: 34px;
    background: var(--orange); color: #fff;
    font-size: 15px; font-weight: 600; letter-spacing: 1px;
    padding: 8px 0 0 40px;
  }
  .role { position: absolute; left: 40px; top: 136px; font-size: 11px; color: var(--orange); }
  .accent { position: absolute; left: 0; top: 0; }

  .contacts { position: absolute; left: 40px; top: 176px; list-style: none; }
  .contacts li { display: flex; align-items: flex-start; gap: 10px; font-size: 15px; margin-bottom: 9px; letter-spacing: 0.5px; }
  .icon {
    flex: none; width: 18px; height: 18px; border-radius: 50%;
    background: var(--orange); display: flex; align-items: center; justify-content: center;
  }
  .icon svg { width: 10px; height: 10px; }

  .social { position: absolute; right: 0; top: 28px; list-style: none; }
  .social li { display: flex; align-items: center; justify-content: flex-end; font-size: 14px; height: 38px; }
  .social__dot { width: 22px; height: 22px; border-radius: 50%; margin-left: 10px; }
  .social__rule { width: 40px; height: 2px; }
  .social .a .social__dot, .social .a .social__rule { background: var(--social-a); }
  .social .b .social__dot, .social .b .social__rule { background: var(--social-b); }
  .social .c .social__dot, .social .c .social__rule { background: var(--social-c); }

  .online { position: absolute; left: 330px; top: 276px; list-style: none; }
  .online li { display: flex; align-items: center; gap: 10px; font-size: 14px; margin-bottom: 10px; }
  .online .icon { width: 16px; height: 16px; background: var(--orange-light); }
</style>
</head>
<body>

<section class="card card--front">
  <svg class="accent" width="640" height="366" viewBox="0 0 640 366" aria-hidden="true">
    <defs>
      <linearGradient id="accent-fade" x1="0" x2="1">
        <stop offset="0" stop-color="#ef5a3a"/>
        <stop offset="1" stop-color="#f39a3c"/>
      </linearGradient>
    </defs>
    <polygon points="262,96 276,96 262,130 248,130" fill="#ef5a3a"/>
    <polygon points="286,96 300,96 286,130 272,130" fill="#ef5a3a"/>
    <polygon points="310,96 324,96 310,130 296,130" fill="#f06a3b"/>
    <polygon points="334,96 348,96 334,130 320,130" fill="#f1783b"/>
    <polygon points="250,126 640,150 640,156 250,130" fill="url(#accent-fade)"/>
  </svg>

  <div class="brand"><span class="brand__dot"></span><span class="brand__name">mosswickpartners</span></div>

  <div class="name-band">HAROLD PENBURY</div>
  <div class="role">Managing Director</div>

  <ul class="contacts">
    <li><span class="icon"><svg viewBox="0 0 10 10"><path d="M2 1 L4 1 L4.6 3 L3.6 3.8 Q4.6 5.6 6.2 6.4 L7 5.4 L9 6 L9 8 Q5 8.6 2.2 5.6 Q1 4 2 1Z" fill="#fff"/></svg></span>0487 263019</li>
    <li><span class="icon"><svg viewBox="0 0 10 10"><rect x="3" y="1" width="4" height="8" rx="0.8" fill="none" stroke="#fff" stroke-width="1.2"/></svg></span>02 9417 3306</li>
    <li><span class="icon"><svg viewBox="0 0 10 10"><path d="M5 9.5 Q1.6 5.6 1.6 3.8 A3.4 3.4 0 0 1 8.4 3.8 Q8.4 5.6 5 9.5Z" fill="#fff"/><circle cx="5" cy="3.8" r="1.2" fill="#ef5a3a"/></svg></span>27 Level 4, Harbour Crest<br>Road NSW</li>
  </ul>

  <ul class="social">
    <li class="a">linkpage.com/mosswick<span class="social__dot"></span><span class="social__rule"></span></li>
    <li class="b">@mosswick<span class="social__dot"></span><span class="social__rule"></span></li>
    <li class="c">Callr<span class="social__dot"></span><span class="social__rule"></span></li>
  </ul>

  <ul class="online">
    <li><span class="icon"><svg viewBox="0 0 10 10"><rect x="1" y="2.5" width="8" height="5.5" fill="none" stroke="#fff" stroke-width="1"/><path d="M1 2.5 L5 5.6 L9 2.5" fill="none" stroke="#fff" stroke-width="1"/></svg></span>harold@mosswick.com</li>
    <li><span class="icon"><svg viewBox="0 0 10 10"><circle cx="5" cy="5" r="3.8" fill="none" stroke="#fff" stroke-width="1"/><path d="M1.2 5 H8.8 M5 1.2 Q2.6 5 5 8.8 Q7.4 5 5 1.2" fill="none" stroke="#fff" stroke-width="0.8"/></svg></span>www.mosswickpartners.com</li>
  </ul>
</section>

<section class="card card--back">
  <div class="brand"><span class="brand__dot"></span><span class="brand__name">mosswickpartners</span></div>
</section>

</body>
</html>
```